The Stone Lantern business cards

Hi
i have attached a photo, this is how i want the front of my business card to look like:
i want the water drop on the right to be orange
and the water drop on the left to be gloss black
"The" and "Pty Ltd." will be in the same orange as the water drop
and "Stone Lantern" will be in white
The background of the logo will be a matte black
on the back of the business card i need the following info:
'The Stone Lantern pty ltd. '
'Plumbing . Drainage . Gas Fitting . Roofing . Jet Blasting . CCTV . '
Also my contact details:
Gus Palmer
0411827396
thestonelantern@mailbarn.example
Licence# 861427D
Target Market(s)
Strata managers, building managers, the general public
Industry/Entity Type
Business

```html
<!DOCTYPE html>
<html lang="en">
<head>
<meta charset="utf-8">
<title>The Stone Lantern – Business Cards</title>
<link rel="stylesheet" href="https://fonts.googleapis.com/css2?family=Arimo:wght@400;700&display=swap">
<style>
  :root {
    --backdrop: #bcbdc0;
    --matte-black: #231f20;
    --orange: #f29f3a;
    --white: #ffffff;
  }
  * { box-sizing: border-box; margin: 0; padding: 0; }
  html, body {
    width: 1200px;
    height: 1014px;
    overflow: hidden;
    background: var(--backdrop);
    font-family: "Arimo", Arial, sans-serif;
  }
  .card {
    position: absolute;
    left: 199px;
    width: 779px;
    height: 450px;
    background: var(--matte-black);
    overflow: hidden;
  }
  .card-front { top: 39px; }
  .card-back { top: 501px; }

  .front-panel {
    position: absolute;
    left: 0; top: 0;
    width: 299px;
    height: 100%;
    background: var(--orange);
  }
  .front-panel svg {
    position: absolute;
    left: 72px; top: 137px;
  }
  .wordmark {
    position: absolute;
    left: 362px;
    top: 104px;
    width: 340px;
    color: var(--white);
    font-weight: 700;
  }
  .wordmark .name span { display: block; line-height: 1; }
  .wordmark .line-the { font-size: 40px; }
  .wordmark .line-stone { font-size: 92px; letter-spacing: -1px; }
  .wordmark .line-lantern { font-size: 62px; letter-spacing: -0.5px; }
  .wordmark .legal {
    display: block;
    text-align: right;
    color: var(--orange);
    font-size: 34px;
    line-height: 1.1;
    margin-top: 4px;
  }

  .contact {
    position: absolute;
    left: 0; right: 0;
    top: 68px;
    text-align: center;
    color: var(--white);
    font-size: 31px;
    line-height: 44px;
  }
  .contact .company {
    color: var(--orange);
    font-weight: 700;
    font-size: 24px;
    margin-bottom: 20px;
  }
  .contact .person {
    font-weight: 700;
    font-size: 32px;
  }
  .services {
    position: absolute;
    left: 0; right: 0; bottom: 0;
    height: 59px;
    background: var(--orange);
    color: var(--white);
    font-size: 26px;
    line-height: 59px;
    text-align: center;
    white-space: nowrap;
  }
</style>
</head>
<body>
  <section class="card card-front">
    <div class="front-panel">
      <svg width="178" height="178" viewBox="0 0 178 178" aria-hidden="true">
        <circle cx="89" cy="89" r="89" fill="var(--matte-black)"/>
      </svg>
    </div>
    <div class="wordmark">
      <p class="name">
        <span class="line-the">THE</span>
        <span class="line-stone">STONE</span>
        <span class="line-lantern">LANTERN</span>
      </p>
      <span class="legal">Pty Ltd.</span>
    </div>
  </section>

  <section class="card card-back">
    <div class="contact">
      <p class="company">The Stone Lantern pty ltd.</p>
      <p class="person">GUS PALMER</p>
      <p class="phone">0411827396</p>
      <p class="email">thestonelantern@mailbarn.example</p>
      <p class="licence">Licence# 861427D</p>
    </div>
    <div class="services">Plumbing . Drainage . Gas Fitting . Roofing . Jet Blasting . CCTV</div>
  </section>
</body>
</html>
```